Swimming Pool Supply Company Business Cards

We need business cards designed for company. These need to be easy to edit so that we can fill in names, titles, and contact info for each person who works here.

Dalton R. Whitfield
Manager of Legal & Finance
K.L. Brisbane, Incorporated

4837 Grenway Avenue
Marlow Heights, PA 19243

E. dalton@klbrisbane-example.com
M. (215) 555-0173
O. (215) 555-0148

Contact Information for Business Card

Looking to upgrade current business cards with graphic that can be edited. Looking for fresh ideas for an age old industry.

Font styles to use
Serif
Sans Serif

Colors

Designer to choose colors to be used in the design.

Requirements
Must have
• Professional, fresh, unique but professional

```html
<!DOCTYPE html>
<html lang="en">
<head>
<meta charset="utf-8">
<title>K.L. Brisbane Business Cards</title>
<link href="https://fonts.googleapis.com/css2?family=Lato:wght@400;700;900&display=swap" rel="stylesheet">
<style>
  :root {
    --bg: #e9e6e3;
    --card-dark: #1c1c1d;
    --card-light: #ffffff;
    --brand-blue: #2f62b8;
    --brand-blue-light: #5b8fd6;
    --ink: #2a2a2a;
    --ink-soft: #555555;
    --on-dark: #d6d6d6;
  }
  * { box-sizing: border-box; margin: 0; padding: 0; }
  html, body { width: 1200px; height: 824px; overflow: hidden; }
  body {
    background: var(--bg);
    font-family: "Lato", sans-serif;
    display: flex;
    align-items: center;
    justify-content: center;
    gap: 40px;
  }
  .card {
    width: 540px;
    height: 309px;
    position: relative;
    box-shadow: 0 10px 28px rgba(0,0,0,0.18);
  }
  .card--back {
    background: var(--card-dark);
    display: flex;
    flex-direction: column;
    align-items: center;
    justify-content: center;
  }
  .wordmark {
    font-weight: 900;
    letter-spacing: 2px;
    line-height: 1;
    text-transform: uppercase;
  }
  .card--back .wordmark { font-size: 58px; color: var(--brand-blue-light); }
  .tagline {
    text-transform: uppercase;
    font-weight: 700;
    letter-spacing: 1px;
  }
  .card--back .tagline { font-size: 12px; color: var(--brand-blue-light); margin-top: 10px; }
  .website {
    font-size: 14px;
    letter-spacing: 3px;
    color: var(--on-dark);
    margin-top: 26px;
  }
  .card--front { background: var(--card-light); padding: 0 34px; }
  .front-logo { position: absolute; left: 34px; top: 84px; }
  .card--front .wordmark { font-size: 38px; color: var(--brand-blue); }
  .card--front .tagline { font-size: 8px; color: var(--brand-blue); margin-top: 6px; }
  .person { position: absolute; left: 300px; top: 78px; }
  .person-name {
    font-size: 20px;
    text-transform: uppercase;
    color: var(--ink);
    letter-spacing: 1px;
  }
  .person-title { font-size: 14px; color: var(--brand-blue); margin-top: 2px; }
  .contact-list { list-style: none; margin-top: 12px; }
  .contact-list li {
    display: flex;
    align-items: center;
    gap: 8px;
    font-size: 14px;
    color: var(--ink-soft);
    margin-bottom: 5px;
  }
  .icon { width: 14px; height: 14px; fill: var(--brand-blue); flex: none; }
  .address {
    position: absolute;
    left: 34px;
    bottom: 36px;
    display: flex;
    align-items: center;
    gap: 8px;
    font-size: 14px;
    color: var(--ink-soft);
  }
</style>
</head>
<body>
  <section class="card card--back">
    <div class="wordmark">BRISBANE</div>
    <div class="tagline">Swimming Pools, Supplies &amp; Accessories</div>
    <div class="website">www.klbrisbane-example.com</div>
  </section>

  <section class="card card--front">
    <div class="front-logo">
      <div class="wordmark">BRISBANE</div>
      <div class="tagline">Swimming Pools, Supplies &amp; Accessories</div>
    </div>

    <div class="person">
      <div class="person-name">Dalton R. Whitfield</div>
      <div class="person-title">Manager of Legal &amp; Finance</div>
      <ul class="contact-list">
        <li>
          <svg class="icon" viewBox="0 0 16 16" aria-hidden="true"><path d="M1 6c0-2 3-3 7-3s7 1 7 3v1h-3V6H4v1H1z M3 8h10l1 6H2z"/></svg>
          (215) 555-0173
        </li>
        <li>
          <svg class="icon" viewBox="0 0 16 16" aria-hidden="true"><path d="M5 1h6a1 1 0 0 1 1 1v12a1 1 0 0 1-1 1H5a1 1 0 0 1-1-1V2a1 1 0 0 1 1-1zm1 2v9h4V3z"/></svg>
          (215) 555-0148
        </li>
        <li>
          <svg class="icon" viewBox="0 0 16 16" aria-hidden="true"><path d="M1 3h14v10H1z M2 4l6 5 6-5" stroke="#fff" stroke-width="1"/></svg>
          dalton@klbrisbane-example.com
        </li>
      </ul>
    </div>

    <div class="address">
      <svg class="icon" viewBox="0 0 16 16" aria-hidden="true"><path d="M8 1a5 5 0 0 1 5 5c0 4-5 9-5 9S3 10 3 6a5 5 0 0 1 5-5zm0 3a2 2 0 1 0 0 4 2 2 0 0 0 0-4z"/></svg>
      4837 Grenway Avenue, Marlow Heights, PA 19243
    </div>
  </section>
</body>
</html>
```